ZiPU Vortal Bhutan Trip

This is a one-page (A5) flyer to attract sign ups for Bhutan Trip.

Target Market(s)

Young entrepreneurs (worldwide)

Requirements
Must have
• Must have "WOW" effect and attract sign ups
Nice to have
• Striking and vibrant

```html
<!DOCTYPE html>
<html lang="en">
<head>
<meta charset="utf-8">
<title>ZiPU Vortal Bhutan Trip</title>
<link href="https://fonts.googleapis.com/css2?family=Crimson+Text:wght@400;600;700&family=Tillana:wght@500&display=swap" rel="stylesheet">
<style>
  :root {
    --sky: #4db8f5;
    --sky-light: #bfe6fb;
    --navy: #2b2e82;
    --orange: #fa5514;
    --yellow: #f0b400;
    --green: #3aaa35;
    --purple: #7b2a8c;
    --indigo: #4b4fc4;
    --pink: #e0246f;
    --cyan: #2aa3d8;
    --red: #e01b1b;
    --ink: #1d1d1d;
    --body: #444;
    --footer: #f2f2f2;
    --white: #ffffff;
  }
  * { margin: 0; padding: 0; box-sizing: border-box; }
  html, body { width: 960px; height: 1200px; overflow: hidden; background: #e9e6e1; }
  .flyer {
    position: relative; width: 960px; height: 1200px; overflow: hidden;
    font-family: "Crimson Text", Georgia, serif; color: var(--ink);
  }
  .flyer-shapes { position: absolute; inset: 0; }
  .brand-name {
    position: absolute; left: 203px; width: 429px; top: 150px; text-align: center;
    font-size: 66px; font-weight: 700; color: var(--navy); letter-spacing: 1px;
  }
  .trip-date {
    position: absolute; right: 40px; top: 166px;
    font-size: 44px; font-weight: 700; color: var(--navy);
  }
  .trip-title {
    position: absolute; right: 40px; top: 205px;
    font-family: "Tillana", cursive; font-weight: 500; font-size: 118px; line-height: 1;
    color: var(--white); -webkit-text-stroke: 3px var(--navy); letter-spacing: 2px;
  }
  .headline {
    position: absolute; left: 40px; width: 880px; top: 692px; text-align: center;
    font-size: 40px; font-weight: 700; line-height: 1.05; color: var(--white);
  }
  .highlights { position: absolute; left: 32px; top: 848px; list-style: none; }
  .highlights li { font-size: 20px; line-height: 34.5px; color: var(--body); }
  .highlights .key { text-transform: uppercase; }
  .k-learn { color: var(--orange); }
  .k-engage { color: var(--yellow); }
  .k-discover { color: var(--purple); }
  .k-savour { color: var(--green); }
  .k-immerse { color: var(--indigo); }
  .k-experience { color: var(--pink); }
  .k-rejuvenate { color: var(--cyan); }
  .price { position: absolute; left: 563px; top: 820px; font-size: 52px; font-weight: 600; color: var(--white); }
  .early-bird { position: absolute; left: 562px; top: 910px; font-size: 25px; font-weight: 700; }
  .early-note { position: absolute; left: 562px; top: 945px; font-size: 18px; }
  .register { position: absolute; left: 562px; top: 996px; font-size: 23px; font-weight: 700; color: var(--red); line-height: 1.12; }
  .contact {
    position: absolute; left: 537px; top: 1062px; width: 440px; height: 46px;
    background: var(--orange); border-radius: 23px 0 0 23px;
    display: flex; align-items: center; padding-left: 38px; gap: 12px;
    font-size: 23px; font-weight: 700; color: var(--white);
  }
  .footer {
    position: absolute; left: 0; top: 1113px; width: 960px; height: 87px; background: var(--footer);
    display: flex; align-items: center; padding-left: 37px;
  }
  .footer-label { font-size: 17px; font-weight: 700; line-height: 1.3; }
  .footer-host { margin-left: 38px; font-size: 26px; font-weight: 700; color: var(--orange); }
  .footer-support { margin-left: 78px; }
  .partner { display: flex; align-items: center; gap: 6px; margin-left: 24px; font-size: 17px; font-weight: 700; color: var(--green); }
  .partner-mark { width: 16px; height: 16px; border-radius: 50%; }
  .p-brightpath .partner-mark { border: 2px solid var(--green); }
  .p-rootwise { color: var(--navy); }
  .p-rootwise .partner-mark { background: var(--navy); }
  .p-trailnova { color: var(--cyan); }
  .p-trailnova .partner-mark { background: var(--orange); }
</style>
</head>
<body>
<div class="flyer">
  <svg class="flyer-shapes" width="960" height="1200" viewBox="0 0 960 1200" xmlns="http://www.w3.org/2000/svg">
    <defs>
      <linearGradient id="sky-scene" x1="0" y1="0" x2="0" y2="1">
        <stop offset="0" stop-color="#45b2f3"/>
        <stop offset="0.45" stop-color="#a9d9f3"/>
        <stop offset="0.7" stop-color="#7f97b3"/>
        <stop offset="1" stop-color="#3f5b82"/>
      </linearGradient>
      <linearGradient id="bridge-scene" x1="0" y1="0" x2="0" y2="1">
        <stop offset="0" stop-color="#6b9a4a"/><stop offset="0.6" stop-color="#5f7e45"/><stop offset="1" stop-color="#8b8f88"/>
      </linearGradient>
      <linearGradient id="temple-scene" x1="0" y1="0" x2="0" y2="1">
        <stop offset="0" stop-color="#8cc1e6"/><stop offset="0.45" stop-color="#c8b8a6"/><stop offset="1" stop-color="#a39c92"/>
      </linearGradient>
      <linearGradient id="cliff-scene" x1="0" y1="0" x2="0" y2="1">
        <stop offset="0" stop-color="#cfd6dc"/><stop offset="0.5" stop-color="#6d8a4e"/><stop offset="1" stop-color="#3f5a32"/>
      </linearGradient>
    </defs>
    <rect class="backdrop-photo" x="0" y="0" width="960" height="700" fill="url(#sky-scene)" role="img" aria-label="Photo of snow-capped Himalayan peaks under a blue sky with clouds"/>
    <rect class="logo-panel" x="203" y="0" width="429" height="330" fill="#ffffff" opacity="0.95"/>
    <path class="accent-orange" d="M0,330 L150,385 L0,420 Z" fill="var(--orange)"/>
    <path class="accent-green" d="M660,420 L700,395 L690,440 Z" fill="var(--green)"/>
    <rect x="0" y="780" width="960" height="420" fill="var(--white)"/>
    <path class="band-yellow" d="M0,600 L960,600 L960,871 C800,830 650,815 480,810 C300,806 150,808 0,815 Z" fill="var(--yellow)"/>
    <path class="band-orange" d="M0,792 C300,760 600,725 960,697 L960,871 C800,830 650,815 480,810 C300,806 150,808 0,815 Z" fill="var(--orange)"/>
    <path class="band-green" d="M590,806 C700,818 850,845 960,871 L960,908 C820,896 700,896 530,902 Z" fill="var(--green)"/>
    <g class="photo-circles" stroke="#ffffff" stroke-width="11">
      <circle cx="152" cy="513" r="180" fill="url(#bridge-scene)" role="img" aria-label="Photo of a suspension bridge with prayer flags leading to a hillside gate"/>
      <circle cx="816" cy="508" r="172" fill="url(#cliff-scene)" role="img" aria-label="Photo of a cliffside monastery among green forest"/>
      <circle cx="487" cy="508" r="176" fill="url(#temple-scene)" role="img" aria-label="Photo of a red-robed monk walking toward a temple courtyard"/>
    </g>
  </svg>

  <div class="brand-name">ZiPU Vortal</div>
  <div class="trip-date">3-6 July 2017</div>
  <h1 class="trip-title">bhutan trip</h1>

  <p class="headline">Sign up for a once in a lifetime experience<br>in the land of happiness!</p>

  <ul class="highlights">
    <li><span class="key k-learn">Learn</span> from Leading Social Change Makers</li>
    <li><span class="key k-engage">Engage</span> the community through volunteering</li>
    <li><span class="key k-discover">Discover</span> your inner happiness</li>
    <li><span class="key k-savour">Savour</span> Organic food</li>
    <li><span class="key k-immerse">Immerse</span> in traditional sports and craft</li>
    <li><span class="key k-experience">Experience</span> warm Bhutanese hospitality</li>
    <li><span class="key k-rejuvenate">Rejuvenate</span> your mind, body and soul</li>
  </ul>

  <div class="price">$2800/-</div>
  <div class="early-bird">Early bird discount $2300/-</div>
  <div class="early-note">(If you sign up by 31 March 2017)</div>
  <div class="register">Register now!<br>Limited to 30 participants!</div>

  <div class="contact">
    <svg width="24" height="18" viewBox="0 0 24 18" aria-hidden="true"><rect x="1" y="1" width="22" height="16" fill="none" stroke="#fff" stroke-width="2"/><path d="M1,1 L12,10 L23,1 M1,17 L9,8 M23,17 L15,8" fill="none" stroke="#fff" stroke-width="1.6"/></svg>
    <span>ravi@brightpathfund.org</span>
  </div>

  <footer class="footer">
    <div class="footer-label">Exclusively Brought<br>To You By:</div>
    <div class="footer-host">ZiPU Vortal</div>
    <div class="footer-label footer-support">Supported By:</div>
    <div class="partner p-brightpath"><span class="partner-mark"></span>Brightpath Fund</div>
    <div class="partner p-rootwise"><span class="partner-mark"></span>Rootwise</div>
    <div class="partner p-trailnova"><span class="partner-mark"></span>Trailnova</div>
  </footer>
</div>
</body>
</html>
```